Business card (AI file uploaded)

We need a business card design that is minimalist using existing logo (attached). Source files must be editable so we can make the same design with other names.

Screenshots included of a design I was working on to give you an idea of the style I would like. Looking for similar modern styles

Thanks

```html
<!DOCTYPE html>
<html lang="en">
<head>
<meta charset="utf-8">
<title>Marlow Law Group – Business Card</title>
<link rel="stylesheet" href="https://fonts.googleapis.com/css2?family=Montserrat:wght@400;500;600&display=swap">
<style>
  :root {
    --backdrop: #d9d7d3;
    --card-light: #f1f1f1;
    --card-dark: #383838;
    --ink: #2e2e2e;
    --ink-soft: #555555;
    --paper: #ffffff;
    --icon-tile: #333333;
  }
  * { margin: 0; padding: 0; box-sizing: border-box; }
  html, body {
    width: 1200px; height: 897px; overflow: hidden;
    background: var(--backdrop);
    font-family: "Montserrat", sans-serif;
  }
  .sheet {
    position: relative; width: 1200px; height: 897px;
    display: flex; align-items: center; justify-content: center; gap: 40px;
  }
  .card {
    position: relative; width: 520px; height: 300px;
    border-radius: 28px; overflow: hidden;
  }
  .card--front { background: var(--card-light); color: var(--ink); }
  .card--back { background: var(--card-dark); color: var(--paper); }

  /* front */
  .contact-list {
    position: absolute; top: 40px; right: 36px;
    list-style: none; display: flex; flex-direction: column; gap: 16px;
  }
  .contact-item { display: flex; align-items: center; gap: 12px; }
  .contact-icon {
    width: 24px; height: 24px; border-radius: 5px; background: var(--icon-tile);
    display: flex; align-items: center; justify-content: center; flex: none;
  }
  .contact-icon svg { width: 14px; height: 14px; }
  .contact-text { font-size: 10px; line-height: 1.35; letter-spacing: 0.04em; color: var(--ink-soft); text-transform: uppercase; }

  .holder { position: absolute; left: 40px; top: 56px; }
  .holder-name { font-size: 13px; letter-spacing: 0.06em; text-transform: uppercase; font-weight: 600; }
  .holder-name span { font-weight: 400; }
  .holder-role { margin-top: 4px; font-size: 9px; letter-spacing: 0.08em; text-transform: uppercase; color: var(--ink-soft); }

  .brand { display: flex; align-items: center; gap: 14px; }
  .brand-dot { width: 44px; height: 44px; border-radius: 50%; background: currentColor; flex: none; }
  .brand-name {
    font-weight: 500; font-size: 22px; letter-spacing: 0.12em; line-height: 1.15; text-transform: uppercase;
  }
  .brand-name small { display: block; font-size: 13px; letter-spacing: 0.32em; font-weight: 500; }
  .card--front .brand { position: absolute; left: 40px; bottom: 46px; color: var(--ink); }

  /* back */
  .card--back .brand {
    position: absolute; inset: 0; flex-direction: column; justify-content: center; gap: 18px; color: var(--paper);
    text-align: center;
  }
  .card--back .brand-dot { width: 56px; height: 56px; }
  .card--back .brand-name { font-size: 28px; }
  .card--back .brand-name small { font-size: 15px; }
</style>
</head>
<body>
<main class="sheet">
  <section class="card card--front" aria-label="Business card front">
    <div class="holder">
      <p class="holder-name">Daniel <span>Carter</span></p>
      <p class="holder-role">Senior Graphic Designer</p>
    </div>

    <div class="brand">
      <span class="brand-dot" aria-hidden="true"></span>
      <p class="brand-name">Marlow<small>Law Group PC</small></p>
    </div>

    <ul class="contact-list">
      <li class="contact-item">
        <span class="contact-icon">
          <svg viewBox="0 0 24 24" fill="#fff"><path d="M6.6 10.8a15.1 15.1 0 0 0 6.6 6.6l2.2-2.2a1 1 0 0 1 1-.25 11.4 11.4 0 0 0 3.6.57 1 1 0 0 1 1 1V20a1 1 0 0 1-1 1A17 17 0 0 1 3 4a1 1 0 0 1 1-1h3.5a1 1 0 0 1 1 1c0 1.25.2 2.45.57 3.6a1 1 0 0 1-.25 1z"/></svg>
        </span>
        <p class="contact-text">020 555 0147<br>020 555 0148</p>
      </li>
      <li class="contact-item">
        <span class="contact-icon">
          <svg viewBox="0 0 24 24" fill="none" stroke="#fff" stroke-width="1.8"><circle cx="12" cy="12" r="9"/><path d="M3 12h18M12 3c3 3.2 3 14.8 0 18M12 3c-3 3.2-3 14.8 0 18"/></svg>
        </span>
        <p class="contact-text">www.marlowlaw.co<br>marlowlaw.co</p>
      </li>
      <li class="contact-item">
        <span class="contact-icon">
          <svg viewBox="0 0 24 24" fill="none" stroke="#fff" stroke-width="1.8"><rect x="3" y="5" width="18" height="14" rx="1"/><path d="M3 6l9 7 9-7"/></svg>
        </span>
        <p class="contact-text">hello@marlowlaw.co<br>office@marlowlaw.co</p>
      </li>
      <li class="contact-item">
        <span class="contact-icon">
          <svg viewBox="0 0 24 24" fill="#fff"><path d="M12 2a7 7 0 0 0-7 7c0 5.2 7 13 7 13s7-7.8 7-13a7 7 0 0 0-7-7zm0 9.5A2.5 2.5 0 1 1 12 6.5a2.5 2.5 0 0 1 0 5z"/></svg>
        </span>
        <p class="contact-text">48 Harbour Lane, Kingsford 4120<br>United Kingdom</p>
      </li>
    </ul>
  </section>

  <section class="card card--back" aria-label="Business card back">
    <div class="brand">
      <span class="brand-dot" aria-hidden="true"></span>
      <p class="brand-name">Marlow<small>Law Group PC</small></p>
    </div>
  </section>
</main>
</body>
</html>
```